Fresh & Clean *NEW* BUSINESS CARD Needed - OPTOMETRY Clinic/Optical

High-tech optometry practice with 3 doctors seeking new business card.  We provide eye exams, sell, designer glasses/contacts/specialty eyewear and treat ocular diseases.  For our business cards, we are seeking fresh, clean, and crisp design as we grow our team (staffing change).  Simply adding doctors is making the card look busy/cluttered.
 Looking for professional, less cluttered look yet still have our logo, doctor names, phone, address, and website....If possible!  :)
Names:
Marcia Trelford, O.D.
Ned Pallister, O.D.
Oona Ferrant, O.D.
Phone: 555-014-2738
Website: www.BrightLensHub.example
Address:  417 Garnet R. Holloway, Maple Crossing, XX 00000
Ultimately we have the main business card with all doctor sames and that card has two versions  (front is always the same).  The back has two designs (1) displays next appointment time/date, (2) for "general use" (non-appointment.)    I have attached what we have used in the past.  
We also need a design template for each team member in our practice with their name, title, and email.   Those should be designed with the "general use" back (see attached).
**Open to entirely new design so don't feel obligated to keep current format.  Need new perspective!  Also including our watermark and some other design features we have consistently used in past in our portfolio.  Included are two options for logos--vertical and horizontal.
**I also would like to remove "Member of Sight Alliance" on our logo if possible**
 Other image files available upon request.

Target Market(s)

New patient & Current Patients

Industry/Entity Type

Optometry

Contact Information for Business Card

High-tech optometry practice with 3 doctors seeking new business card.  We provide eye exams, sell, designer glasses/contacts/specialty eyewear and treat ocular diseases.  For our business cards, we are seeking fresh, clean, and crisp design as we grow our team (staffing change).  Simply adding doctors is making the card look busy/cluttered.  Looking for professional, less cluttered look yet still have our logo, doctor names, phone, address, and website....If possible!  :) Names: Marcia Trelford, O.D. Ned Pallister, O.D. Oona Ferrant, O.D. Phone: 555-014-2738 Website: www.BrightLensHub.example Address:  417 Garnet R. Holloway, Maple Crossing, XX 00000 Ultimately we have the main business card with all doctor sames and that card has two versions  (front is always the same).  The back has two designs (1) displays next appointment time/date, (2) for "general use" (non-appointment.)    I have attached what we have used in the past.   We also need a design template for each team member in our practice with their name, title, and email.   Those should be designed with the "general use" back (see attached). **Open to entirely new design so don't feel obligated to keep current format.  Need new perspective!  Also including our watermark and some other design features we have consistently used in past in our portfolio.  Included are two options for logos--vertical and horizontal. **I also would like to remove "Member of Sight Alliance" on our logo if possible**  Other image files available upon request.

Font styles to use
Other font styles liked:
• We have used Montserrat / Yellowtail in the past

Colors

Designer to choose colors to be used in the design.

Requirements
Must have
• Clean & Fresh Design with Logo / Info provided in description. Horizontal orientation. **I have included the CMYK colors we currently have in our logo.
Should not have
• Cluttered

```html
<!DOCTYPE html>
<html lang="en">
<head>
<meta charset="utf-8">
<title>Bright Lens Hub – Business Cards</title>
<link rel="stylesheet" href="https://fonts.googleapis.com/css2?family=Montserrat:wght@300;400;600;700&display=swap">
<style>
  :root {
    --stage: #3a3a3c;
    --card: #000000;
    --grey: #8c8c8c;
    --light: #d8d8d8;
    --gold: #e6b51e;
    --sky: #a7dbe9;
    --slate: #2e3944;
    --olive: #6c6a12;
    --amber: #8c5a09;
    --maroon: #3b0c07;
    --halo: #17262b;
  }
  * { box-sizing: border-box; margin: 0; padding: 0; }
  html, body { width: 1200px; height: 875px; overflow: hidden; }
  body {
    background: var(--stage);
    font-family: "Montserrat", sans-serif;
    display: flex;
    align-items: center;
    justify-content: center;
    gap: 40px;
  }
  .card {
    position: relative;
    width: 540px;
    height: 310px;
    background: var(--card);
    border-radius: 20px;
    overflow: hidden;
  }
  .card__band {
    position: absolute;
    left: 0; right: 0; bottom: 0;
    height: 9px;
    display: flex;
  }
  .card__band span { flex: 1; }
  .band-slate { background: var(--slate); }
  .band-sky { background: var(--sky); }
  .band-olive { background: var(--olive); }
  .band-amber { background: var(--amber); }
  .band-maroon { background: var(--maroon); }

  .brand {
    position: absolute;
    display: flex;
    align-items: center;
    gap: 14px;
  }
  .brand__dot {
    width: 34px; height: 34px;
    border-radius: 50%;
    background: var(--sky);
    flex: none;
  }
  .brand__name {
    font-weight: 300;
    font-size: 44px;
    letter-spacing: 1px;
    color: var(--grey);
    line-height: 1;
  }

  /* appointment back */
  .appointment .brand { left: 30px; top: 36px; }
  .appointment__halo {
    position: absolute;
    left: 185px; top: 70px;
    width: 210px; height: 210px;
    border-radius: 50%;
    background: var(--halo);
    opacity: .8;
  }
  .appointment__title {
    position: absolute;
    left: 0; right: 0; top: 108px;
    text-align: center;
    color: var(--gold);
    font-weight: 700;
    font-size: 20px;
  }
  .appointment__fields {
    position: absolute;
    left: 34px; right: 34px; top: 158px;
    display: flex;
    gap: 10px;
    color: var(--light);
    font-size: 16px;
    font-weight: 300;
  }
  .field { display: flex; align-items: flex-end; flex: 1; }
  .field__line {
    flex: 1;
    border-bottom: 2px dotted var(--light);
    margin-left: 4px;
    margin-bottom: 4px;
  }
  .appointment__notice {
    position: absolute;
    left: 0; right: 0; top: 204px;
    text-align: center;
    color: var(--sky);
    font-weight: 700;
    font-size: 19px;
    line-height: 1.3;
  }

  /* general front */
  .front .brand { left: 36px; top: 44px; }
  .front__body {
    position: absolute;
    left: 26px; right: 20px; top: 140px;
    display: flex;
    align-items: center;
  }
  .doctors {
    list-style: none;
    text-align: right;
    color: var(--grey);
    font-weight: 700;
    font-size: 17px;
    line-height: 1.45;
    padding-right: 16px;
    border-right: 1px solid var(--olive);
    white-space: nowrap;
  }
  .contact {
    list-style: none;
    padding-left: 14px;
    color: var(--light);
    font-size: 13px;
    font-weight: 400;
    line-height: 1.55;
    white-space: nowrap;
  }
  .contact li { display: flex; align-items: flex-start; gap: 8px; }
  .contact svg { width: 13px; height: 13px; flex: none; margin-top: 3px; fill: var(--gold); }
</style>
</head>
<body>

<section class="card appointment" aria-label="Appointment reminder card back">
  <div class="appointment__halo" aria-hidden="true"></div>
  <div class="brand">
    <span class="brand__dot"></span>
    <span class="brand__name">brightlenshub</span>
  </div>
  <h2 class="appointment__title">Your Next Appointment</h2>
  <div class="appointment__fields">
    <div class="field">Date<span class="field__line"></span></div>
    <div class="field">Time<span class="field__line"></span></div>
  </div>
  <p class="appointment__notice">If you unable to keep your appointment<br>kindly give us 24 hour notice</p>
  <div class="card__band"><span class="band-slate"></span><span class="band-sky"></span><span class="band-olive"></span><span class="band-amber"></span><span class="band-maroon"></span></div>
</section>

<section class="card front" aria-label="Business card front">
  <div class="brand">
    <span class="brand__dot"></span>
    <span class="brand__name">brightlenshub</span>
  </div>
  <div class="front__body">
    <ul class="doctors">
      <li>Marcia Trelford, O.D.</li>
      <li>Ned Pallister, O.D.</li>
      <li>Oona Ferrant, O.D.</li>
    </ul>
    <ul class="contact">
      <li>
        <svg viewBox="0 0 24 24" aria-hidden="true"><path d="M6.6 10.8a15.1 15.1 0 0 0 6.6 6.6l2.2-2.2a1 1 0 0 1 1-.25 11.4 11.4 0 0 0 3.6.57 1 1 0 0 1 1 1V20a1 1 0 0 1-1 1A17 17 0 0 1 3 4a1 1 0 0 1 1-1h3.5a1 1 0 0 1 1 1c0 1.25.2 2.450.57 3.6a1 1 0 0 1-.25 1z"/></svg>
        <span>555-014-2738</span>
      </li>
      <li>
        <svg viewBox="0 0 24 24" aria-hidden="true"><path d="M12 2a10 10 0 1 0 0 20 10 10 0 0 0 0-20zm6.9 6h-3a15.7 15.7 0 0 0-1.4-3.6A8 8 0 0 1 18.9 8zM12 4c.8 1.2 1.5 2.5 1.9 4h-3.8c.4-1.5 1.1-2.8 1.9-4zM4.3 14a8 8 0 0 1 0-4h3.4a16 16 0 0 0 0 4zm.8 2h3a15.7 15.7 0 0 0 1.4 3.6A8 8 0 0 1 5.1 16zm3-8h-3a8 8 0 0 1 4.4-3.6A15.7 15.7 0 0 0 8.1 8zM12 20c-.8-1.2-1.5-2.5-1.9-4h3.8c-.4 1.5-1.1 2.8-1.9 4zm2.3-6H9.7a14.7 14.7 0 0 1 0-4h4.6a14.7 14.7 0 0 1 0 4zm.2 5.6A15.7 15.7 0 0 0 15.9 16h3a8 8 0 0 1-4.4 3.6zM16.3 14a16 16 0 0 0 0-4h3.4a8 8 0 0 1 0 4z"/></svg>
        <span>www.BrightLensHub.example</span>
      </li>
      <li>
        <svg viewBox="0 0 24 24" aria-hidden="true"><path d="M12 2a7 7 0 0 0-7 7c0 5.25 7 13 7 13s7-7.75 7-13a7 7 0 0 0-7-7zm0 9.5A2.5 2.5 0 1 1 12 6.5a2.5 2.5 0 0 1 0 5z"/></svg>
        <span>417 Garnet R. Holloway,<br>Maple Crossing, XX 00000</span>
      </li>
    </ul>
  </div>
  <div class="card__band"><span class="band-slate"></span><span class="band-sky"></span><span class="band-olive"></span><span class="band-amber"></span><span class="band-maroon"></span></div>
</section>

</body>
</html>
```